Staffing Company Website

We need a website for a new company based out of central California called "Harbor Field Staffing". We staff truck drivers for agriculture trucking businesses. We don't want a super corporate feel, we want something that feels more inviting to the kind of person who would work in Agriculture/Trucking while still being professional. Please let me know if you have any questions

```html
<!DOCTYPE html>
<html lang="en">
<head>
<meta charset="utf-8">
<title>Harbor Field Staffing</title>
<link href="https://fonts.googleapis.com/css2?family=Outfit:wght@300;400;500;600;700&display=swap" rel="stylesheet">
<style>
:root{
  --ink:#141414;
  --charcoal:#1f1f1f;
  --slate:#32353a;
  --night:#151515;
  --footer:#0f0f0f;
  --bar:#1c1c1c;
  --white:#ffffff;
  --muted:#4a4a4a;
  --soft:#dcdcdc;
  --gold:#f2b705;
  --field:#7d9a2c;
}
*{margin:0;padding:0;box-sizing:border-box}
html,body{width:1200px;height:4789px;overflow:hidden}
body{font-family:'Outfit',sans-serif;color:var(--ink);background:var(--white);position:relative}
section,header,footer{position:absolute;left:0;width:1200px;overflow:hidden}
.abs{position:absolute}

/* header */
.site-header{top:0;height:100px;background:#262626;z-index:3}
.brand{position:absolute;left:70px;top:22px;display:flex;align-items:center;gap:14px;color:var(--white)}
.brand-dot{width:44px;height:44px;border-radius:50%;background:var(--white)}
.brand-name{font-size:16px;font-weight:500;line-height:19px;text-transform:uppercase;color:var(--white)}
.main-nav{position:absolute;right:66px;top:40px;display:flex;gap:35px}
.main-nav a{color:var(--white);text-decoration:none;font-size:13px;font-weight:500;letter-spacing:.2px}

/* buttons */
.btn{position:absolute;display:flex;align-items:center;gap:22px;height:64px;padding-left:6px;border-radius:8px 32px 32px 8px;background:var(--charcoal);color:var(--white);font-size:17px;font-weight:500;text-transform:uppercase;text-decoration:none}
.btn .btn-dot{width:52px;height:52px;border-radius:50%;background:var(--white)}
.btn.small{height:50px;font-size:14px;gap:18px}
.btn.small .btn-dot{width:40px;height:40px}
.btn.slate{background:var(--slate)}
.btn.light{background:var(--white);color:var(--ink)}
.btn.light .btn-dot{background:var(--ink)}
.btn.outline{background:transparent;border:2px solid var(--white)}

/* section headings */
.mark-line{position:absolute;display:flex;align-items:center;gap:10px}
.mark-line i{display:block;width:76px;height:2px;background:currentColor}
.mark-line b{display:block;width:20px;height:20px;border-radius:50%;border:2px solid currentColor}
.section-title{position:absolute;left:0;width:1200px;text-align:center;font-size:48px;font-weight:600;letter-spacing:.5px;text-transform:uppercase}

/* hero */
.hero{top:100px;height:610px}
.hero-photo{position:absolute;inset:0;background:linear-gradient(180deg,#e9e6dc 0%,#d9d6c4 38%,#a9b45a 62%,#6f8a24 80%,#4e6b18 100%)}
.hero-machine{position:absolute;left:590px;top:50px;width:560px;height:470px;border-radius:40px;background:radial-gradient(ellipse at 50% 45%,#b94a2a 0%,#6b3020 45%,rgba(40,40,40,.0) 75%)}
.hero-title{position:absolute;left:178px;top:100px;font-size:58px;font-weight:600;line-height:66px;text-transform:uppercase;color:var(--ink)}
.hero-text{position:absolute;left:182px;top:236px;width:440px;font-size:16px;line-height:26px;color:var(--ink)}
.hero-dots{position:absolute;left:572px;top:518px;display:flex;gap:6px}
.hero-dots span{width:10px;height:10px;border-radius:50%;background:rgba(255,255,255,.6)}
.hero-dots span:first-child{background:var(--white)}

/* about */
.about{top:710px;height:639px;background:var(--white)}
.about-photo{position:absolute;left:10px;top:0;width:560px;height:600px;background:radial-gradient(ellipse at 52% 50%,#5f8a5a 0%,#a7c0a2 35%,#e9eeea 62%,#ffffff 80%)}
.about .mark-line{left:616px;top:130px;color:var(--ink)}
.about h2{position:absolute;left:616px;top:155px;font-size:48px;font-weight:600;text-transform:uppercase}
.about p{position:absolute;left:616px;top:232px;width:466px;font-size:13px;line-height:28px;color:var(--muted);text-align:justify}

/* why choose */
.why{top:1349px;height:713px;background:var(--night)}
.why-photo{position:absolute;inset:0;background:radial-gradient(ellipse at 50% 20%,#3b3d33 0%,#25271f 45%,#161614 100%)}
.why .mark-line{left:500px;top:105px;color:var(--white)}
.why .section-title{top:130px;color:var(--white)}
.portrait-ring{position:absolute;left:425px;top:248px;width:350px;height:350px;border-radius:50%;border:3px solid var(--white)}
.portrait{position:absolute;left:24px;top:24px;width:296px;height:296px;border-radius:50%;background:linear-gradient(160deg,#8a9aa8 0%,#5c6470 45%,#8a3b3b 75%,#3a3030 100%)}
.feature-icon{position:absolute;width:116px;height:116px;border-radius:50%;background:var(--white);display:flex;align-items:center;justify-content:center}
.feature-icon::before{content:"";position:absolute;inset:6px;border-radius:50%;border:2px solid var(--ink)}
.feature-icon svg{width:54px;height:54px;position:relative}
.feature-label{position:absolute;color:var(--white);font-size:23px;font-weight:400;line-height:32px}
.feature-label.left{text-align:right}

/* services */
.services{top:2062px;height:1071px;background:var(--white)}
.services .mark-line{left:500px;top:100px;color:var(--ink)}
.services .section-title{top:130px}
.service-card{position:absolute;top:267px;width:336px;height:489px;background:var(--white);border-radius:0 0 56px 0;box-shadow:0 6px 14px rgba(0,0,0,.16);overflow:hidden}
.service-photo{height:242px;border-radius:0 0 56px 0}
.service-card h3{margin-top:30px;text-align:center;font-size:23px;font-weight:500}
.service-card p{margin:20px 36px 0;text-align:justify;font-size:13px;line-height:24px;color:var(--muted)}
.service-card a{display:block;margin-top:22px;text-align:center;font-size:16px;font-weight:600;font-style:italic;color:var(--ink)}

/* call to action */
.cta{top:3133px;height:561px;background:var(--night)}
.cta-photo{position:absolute;inset:0;background:linear-gradient(90deg,#1a1614 0%,#2a211c 40%,#4a3a2c 62%,#6b4a2a 78%,#2a2420 100%)}
.cta .mark-line{left:118px;top:92px;color:var(--white)}
.cta .mark-line i{width:74px}
.cta h2{position:absolute;left:120px;top:120px;width:660px;color:var(--white);font-size:52px;font-weight:400;line-height:63px}

/* testimonials */
.testimonials{top:3694px;height:683px;background:var(--white)}
.testimonials .mark-line{left:500px;top:120px;color:var(--ink)}
.testimonials .section-title{top:150px}
.review{position:absolute;top:270px;width:440px;height:150px}
.avatar{position:absolute;left:0;top:0;width:106px;height:106px;border-radius:50%;background:linear-gradient(180deg,#c9c2b6 0%,#8a7b6a 100%)}
.review blockquote{position:absolute;left:128px;top:6px;width:282px;font-size:13px;line-height:23px;color:var(--muted);text-align:justify}
.review blockquote::before{content:"\201C";font-size:30px;font-weight:700;color:var(--ink);line-height:0;vertical-align:-9px;margin-right:10px}
.review .who{position:absolute;left:128px;top:140px;font-size:20px;font-weight:500}
.review .stars{position:absolute;left:128px;top:168px;font-size:12px;letter-spacing:1px;color:var(--gold)}
.arrow{position:absolute;top:4033px;width:42px;height:42px;border-radius:50%;display:flex;align-items:center;justify-content:center}
.arrow.prev{left:71px;background:var(--white);box-shadow:0 2px 8px rgba(0,0,0,.2)}
.arrow.next{left:1093px;background:var(--slate)}

/* footer */
.site-footer{top:4377px;height:342px;background:var(--footer);color:var(--white)}
.footer-brand{position:absolute;left:494px;top:60px;display:flex;align-items:center;gap:16px}
.footer-brand .brand-dot{width:60px;height:60px}
.footer-brand .brand-name{font-size:21px;line-height:26px}
.contact-row{position:absolute;top:183px;left:238px;display:flex;gap:56px}
.contact-item{display:flex;align-items:center;gap:14px;font-size:13px;line-height:18px}
.contact-icon{width:30px;height:30px;border-radius:4px;border:1px solid #bbb;display:flex;align-items:center;justify-content:center}
.footer-rule{position:absolute;left:68px;top:261px;width:1064px;height:1px;background:#444}
.footer-nav{position:absolute;top:293px;left:213px;display:flex;gap:58px}
.footer-nav a{color:var(--white);text-decoration:none;font-size:13px;font-weight:500}
.legal-bar{position:absolute;top:4719px;left:0;width:1200px;height:70px;background:var(--bar);color:#ddd}
.legal-bar p{position:absolute;left:68px;top:26px;font-size:11px}
.socials{position:absolute;right:66px;top:22px;display:flex;gap:6px}
.socials span{width:26px;height:26px;border:1px solid #ccc;border-radius:3px;display:flex;align-items:center;justify-content:center}
.socials span::after{content:"";width:10px;height:10px;background:#ccc;border-radius:2px}
</style>
</head>
<body>

<header class="site-header">
  <div class="brand"><span class="brand-dot"></span><span class="brand-name">Harbor<br>Field<br>Staffing</span></div>
  <nav class="main-nav">
    <a href="#">HOME</a><a href="#">ABOUT US</a><a href="#">SERVICES</a><a href="#">WHY CHOOSE US?</a><a href="#">TESTIMONIALS</a><a href="#">CONTACT US</a>
  </nav>
</header>

<section class="hero">
  <div class="hero-photo" role="img" aria-label="Red tractor standing in a green grain field at sunrise"></div>
  <div class="hero-machine"></div>
  <h1 class="hero-title">Harbor Field<br>Staffing</h1>
  <p class="hero-text">Lorem ipsum dolor sit amet, consectetur adipiscing elit, sed do eiusmod tempor incididunt ut labore et</p>
  <a class="btn" href="#" style="left:180px;top:306px;width:218px"><span class="btn-dot"></span>Apply Now</a>
  <div class="hero-dots"><span></span><span></span><span></span><span></span></div>
</section>

<section class="about">
  <div class="about-photo" role="img" aria-label="Farmer standing beside a green combine harvester in a field"></div>
  <div class="mark-line"><b></b><i></i></div>
  <h2>About Us</h2>
  <p>Lorem ipsum dolor sit amet, consectetur adipiscing elit, sed do eiusmod tempor incididunt ut labore et dolore magna aliqua. Ut enim ad minim veniam, quis nostrud exercitation ullamco laboris nisi ut aliquip ex ea commodo consequat. Duis aute irure dolor in reprehenderit in voluptate velit esse cillum dolore eu fugiat nulla pariatur. Excepteur sint occaecat cupidatat non proident, sunt in culpa qui officia deserunt mollit anim id est laborum.</p>
  <a class="btn small slate" href="#" style="left:616px;top:456px;width:172px"><span class="btn-dot"></span>Read More</a>
</section>

<section class="why">
  <div class="why-photo" role="img" aria-label="Dark green farm fields and hills at dusk"></div>
  <div class="mark-line"><i></i><b></b><i></i></div>
  <h2 class="section-title">Why Choose Us?</h2>

  <div class="portrait-ring"><div class="portrait" role="img" aria-label="Truck driver in a plaid shirt and cap standing by his truck"></div></div>

  <p class="feature-label left" style="left:30px;top:316px;width:218px">Experienced Staff</p>
  <div class="feature-icon" style="left:278px;top:274px">
    <svg viewBox="0 0 54 54"><circle cx="27" cy="17" r="7" fill="#141414"/><circle cx="14" cy="21" r="5" fill="#141414"/><circle cx="40" cy="21" r="5" fill="#141414"/><path d="M15 42c0-8 5-14 12-14s12 6 12 14z" fill="#141414"/><path d="M4 40c0-6 4-11 10-11 2 0 3 0 4 1-3 3-4 6-4 10z" fill="#141414"/><path d="M50 40c0-6-4-11-10-11-2 0-3 0-4 1 3 3 4 6 4 10z" fill="#141414"/></svg>
  </div>

  <p class="feature-label left" style="left:20px;top:462px;width:228px">Knowledge of<br>basic simple vehicle<br>maintenance</p>
  <div class="feature-icon" style="left:278px;top:453px">
    <svg viewBox="0 0 54 54"><rect x="4" y="16" width="28" height="20" fill="#141414"/><path d="M32 22h9l7 8v6H32z" fill="#141414"/><circle cx="13" cy="40" r="4.5" fill="#141414" stroke="#fff" stroke-width="2"/><circle cx="40" cy="40" r="4.5" fill="#141414" stroke="#fff" stroke-width="2"/></svg>
  </div>

  <div class="feature-icon" style="left:810px;top:274px">
    <svg viewBox="0 0 54 54"><circle cx="27" cy="24" r="15" fill="none" stroke="#141414" stroke-width="5"/><circle cx="27" cy="24" r="4" fill="#141414"/><path d="M13 26h10M31 26h10M27 28v10" stroke="#141414" stroke-width="4"/><path d="M6 34l8 14h8M48 34l-8 14h-8" fill="none" stroke="#141414" stroke-width="3"/></svg>
  </div>
  <p class="feature-label" style="left:955px;top:298px;width:200px">A clean, safe<br>driving record</p>

  <div class="feature-icon" style="left:810px;top:453px">
    <svg viewBox="0 0 54 54"><circle cx="20" cy="16" r="8" fill="none" stroke="#141414" stroke-width="4" stroke-dasharray="4 2"/><rect x="4" y="26" width="30" height="14" fill="#141414"/><path d="M34 30h8l6 6v4H34z" fill="#141414"/><circle cx="12" cy="43" r="4" fill="#141414" stroke="#fff" stroke-width="2"/><circle cx="40" cy="43" r="4" fill="#141414" stroke="#fff" stroke-width="2"/></svg>
  </div>
  <p class="feature-label" style="left:955px;top:475px;width:200px">Supply Chain<br>Efficiency</p>
</section>

<section class="services">
  <div class="mark-line"><i></i><b></b><i></i></div>
  <h2 class="section-title">Our Services</h2>

  <article class="service-card" style="left:70px">
    <div class="service-photo" role="img" aria-label="Smiling driver at the wheel inside a truck cab" style="background:linear-gradient(135deg,#5a6e86 0%,#b8c4cc 45%,#8a4040 70%,#2a2a2a 100%)"></div>
    <h3>Service Name 1</h3>
    <p>Lorem ipsum dolor sit amet, consectetur adipiscing elit. Sed blandit laoreet risus ac hendrerit. Suspendisse nec euismod</p>
    <a href="#">Read More</a>
  </article>
  <article class="service-card" style="left:434px">
    <div class="service-photo" role="img" aria-label="Driver leaning out of the window of a blue truck" style="background:linear-gradient(135deg,#2a4aa0 0%,#8aa6d0 40%,#3a4a70 70%,#1a1a2a 100%)"></div>
    <h3>Service Name 2</h3>
    <p>Lorem ipsum dolor sit amet, consectetur adipiscing elit. Sed blandit laoreet risus ac hendrerit. Suspendisse nec euismod</p>
    <a href="#">Read More</a>
  </article>
  <article class="service-card" style="left:796px">
    <div class="service-photo" role="img" aria-label="Woman driving a truck seen from the passenger seat" style="background:linear-gradient(135deg,#3a3a3a 0%,#9aa0a8 45%,#2e4a8a 65%,#1a1a1a 100%)"></div>
    <h3>Service Name 3</h3>
    <p>Lorem ipsum dolor sit amet, consectetur adipiscing elit. Sed blandit laoreet risus ac hendrerit. Suspendisse nec euismod</p>
    <a href="#">Read More</a>
  </article>

  <a class="btn slate" href="#" style="left:492px;top:822px;width:216px"><span class="btn-dot"></span>View More</a>
</section>

<section class="cta">
  <div class="cta-photo" role="img" aria-label="Line of semi trucks parked at sunset"></div>
  <div class="mark-line"><b></b><i></i></div>
  <h2>Are You Looking For Truck Drivers For Agriculture Trucking Businesses</h2>
  <a class="btn light" href="#" style="left:115px;top:350px;width:214px;gap:18px"><span class="btn-dot"></span>Contact Us</a>
  <a class="btn outline" href="#" style="left:352px;top:350px;width:216px;gap:18px"><span class="btn-dot"></span>Apply Now</a>
</section>

<section class="testimonials">
  <div class="mark-line"><i></i><b></b><i></i></div>
  <h2 class="section-title">Our Testimonials</h2>

  <div class="review" style="left:160px">
    <div class="avatar" role="img" aria-label="Portrait of a client"></div>
    <blockquote>Lorem ipsum dolor sit amet, consectetur adipiscing elit. Maece nas ac tellus ac ipsum porta viverra sit amet sed leo. Vivamus eu mauris convallis, hendrerit</blockquote>
    <p class="who">Dale Whitaker</p>
    <p class="stars">★★★★★</p>
  </div>
  <div class="review" style="left:636px">
    <div class="avatar" role="img" aria-label="Portrait of a client" style="background:linear-gradient(180deg,#d8c8b8 0%,#8a5a3a 100%)"></div>
    <blockquote>Lorem ipsum dolor sit amet, consectetur adipiscing elit. Maece nas ac tellus ac ipsum porta viverra sit amet sed leo. Vivamus eu mauris convallis, hendrerit</blockquote>
    <p class="who">Rosa Mendez</p>
    <p class="stars">★★★★★</p>
  </div>

  <a class="btn slate" href="#" style="left:492px;top:498px;width:216px"><span class="btn-dot"></span>View More</a>
</section>

<span class="arrow prev"><svg width="16" height="12" viewBox="0 0 16 12"><path d="M15 6H2M6 1L1 6l5 5" fill="none" stroke="#141414" stroke-width="2"/></svg></span>
<span class="arrow next"><svg width="16" height="12" viewBox="0 0 16 12"><path d="M1 6h13M10 1l5 5-5 5" fill="none" stroke="#fff" stroke-width="2"/></svg></span>

<footer class="site-footer">
  <div class="footer-brand"><span class="brand-dot"></span><span class="brand-name">Harbor<br>Field<br>Staffing</span></div>
  <div class="contact-row">
    <div class="contact-item"><span class="contact-icon"><svg width="14" height="14" viewBox="0 0 14 14"><path d="M3 1l2 3-1.5 1.5c.8 1.8 2.2 3.2 4 4L9 8l3 2-1 3C6 13 1 8 1 3z" fill="none" stroke="#fff" stroke-width="1.3"/></svg></span><span>CALL US<br>(559) 010-4427</span></div>
    <div class="contact-item"><span class="contact-icon"><svg width="14" height="12" viewBox="0 0 14 12"><rect x="1" y="1" width="12" height="10" fill="#fff"/><path d="M1 1l6 5 6-5" fill="none" stroke="#0f0f0f" stroke-width="1.3"/></svg></span><span>EMAIL US<br>hello@harborfield.example</span></div>
    <div class="contact-item"><span class="contact-icon"><svg width="12" height="16" viewBox="0 0 12 16"><path d="M6 15S1 9 1 6a5 5 0 0110 0c0 3-5 9-5 9z" fill="#fff"/><circle cx="6" cy="6" r="2" fill="#0f0f0f"/></svg></span><span>Address line Dummy Here<br>Address line Here</span></div>
  </div>
  <div class="footer-rule"></div>
  <nav class="footer-nav">
    <a href="#">HOME</a><a href="#">ABOUT US</a><a href="#">SERVICES</a><a href="#">WHY CHOOSE US?</a><a href="#">TESTIMONIALS</a><a href="#">CONTACT US</a>
  </nav>
</footer>

<div class="legal-bar">
  <p>Copyright © 2024 All Rights Reserved By Harbor Field Staffing</p>
  <div class="socials"><span></span><span></span><span></span><span></span></div>
</div>

</body>
</html>
```